IT business looking for Standout Letterhead Design

We need a letterhead design for a company based in San Diego, CA called Corvane Systems, Inc. We specialize in IT engineering, installation and technical support pertaining to the department of defense.

We would like to see a design that incorporates the black and gold that matches our company logo.

More information on the company can be found at www.corvane-sys.example

```html
<!DOCTYPE html>
<html lang="en">
<head>
<meta charset="utf-8">
<title>Corvane Systems, Inc. — Letterhead</title>
<link rel="stylesheet" href="https://fonts.googleapis.com/css2?family=Forum&family=Tinos&display=swap">
<style>
  :root {
    --ink: #111111;
    --gold: #dcb41e;
    --paper: #ffffff;
    --mark-faint: #ebebeb;
    --mark-faint-gold: #f6ecc4;
  }
  * { margin: 0; padding: 0; box-sizing: border-box; }
  html, body { width: 873px; height: 1200px; overflow: hidden; background: var(--paper); }
  .letterhead {
    position: relative;
    width: 873px;
    height: 1200px;
    background: var(--paper);
    color: var(--ink);
    font-family: "Tinos", "Times New Roman", serif;
  }
  .brand-mark {
    position: absolute;
    left: 20px;
    top: 40px;
    width: 240px;
    display: flex;
    flex-direction: column;
    align-items: center;
  }
  .brand-mark__dot {
    width: 80px;
    height: 80px;
    border-radius: 50%;
    background: var(--gold);
    margin-bottom: 22px;
  }
  .brand-mark__name {
    font-family: "Tinos", "Times New Roman", serif;
    font-size: 44px;
    line-height: 1;
    color: var(--ink);
  }
  .company-name {
    position: absolute;
    left: 288px;
    top: 62px;
    width: 560px;
    font-family: "Forum", Georgia, serif;
    font-weight: 400;
    font-size: 51px;
    line-height: 1;
    white-space: nowrap;
  }
  .company-city {
    position: absolute;
    left: 460px;
    top: 130px;
    font-size: 20px;
  }
  .contact {
    position: absolute;
    top: 165px;
    font-size: 15px;
    line-height: 20px;
  }
  .contact--left { left: 304px; }
  .contact--right { left: 650px; }
  .rule {
    position: absolute;
    left: 0;
    width: 873px;
    height: 7px;
    background: var(--gold);
  }
  .rule--top { top: 237px; }
  .rule--bottom { top: 1144px; }
  .background-mark {
    position: absolute;
    left: 0;
    top: 500px;
    width: 873px;
    height: 280px;
    display: flex;
    align-items: center;
    justify-content: center;
    gap: 36px;
  }
  .background-mark__dot {
    width: 220px;
    height: 220px;
    border-radius: 50%;
    background: var(--mark-faint-gold);
  }
  .background-mark__name {
    font-family: "Tinos", "Times New Roman", serif;
    font-size: 80px;
    line-height: 1;
    color: var(--mark-faint);
  }
  .address {
    position: absolute;
    top: 1158px;
    left: 0;
    width: 873px;
    text-align: center;
    font-size: 17px;
  }
</style>
</head>
<body>
  <main class="letterhead">
    <div class="brand-mark">
      <span class="brand-mark__dot"></span>
      <span class="brand-mark__name">Corvane</span>
    </div>

    <h1 class="company-name">Corvane Systems, Inc.</h1>
    <p class="company-city">San Diego, California</p>

    <p class="contact contact--left">Website: www.corvane-sys.example<br>Tel: 619-555-0142</p>
    <p class="contact contact--right">Email:&nbsp; info@corvane-sys.example<br>Telefax: 619-555-0187</p>

    <div class="rule rule--top"></div>

    <div class="background-mark" aria-hidden="true">
      <div class="background-mark__dot"></div>
      <div class="background-mark__name">Corvane</div>
    </div>

    <div class="rule rule--bottom"></div>
    <p class="address">418 Harbor Ridge Lane, Chula Vista, CA 91915</p>
  </main>
</body>
</html>
```